Funny Real Estate Marketing Banner Ad

I'm a Real Estate agent in Vancouver, BC. I've provided 3 photos, two recent (one in colour and one in black & white) and one from 1990. I'd like an ad with a catchy tagline, e.g. (Keeping it "real" estate since the 90's), integrating one recent and one past photo. The ad should be funny but professional. It will need to be in a few different formats (320 x250, 320 x 50, 1200 x 628 & 728 x 90). It might be preferable to use the existing black and white photo, given that they look more similar.
Updates

Target Market(s)

Home Buyers and Sellers

Industry/Entity Type

Real Estate Agent

Requirements
Must have
• Would like it to match my current website colours - www.agentmorvyn.net.
• Catchy Tagline.
• My Name, phone # and web address.

```html
<!DOCTYPE html>
<html lang="en">
<head>
<meta charset="utf-8">
<title>Banner Design Set – Morvyn Hale</title>
<link href="https://fonts.googleapis.com/css2?family=Open+Sans:wght@300;400;600;700&display=swap" rel="stylesheet">
<style>
:root{
  --board:#121212;
  --board-light:#1c1c1c;
  --sky:#1fb0e6;
  --sky-deep:#4d93b8;
  --panel:#f2f3f4;
  --ink:#111111;
  --accent:#29aee6;
  --brand:#1d3f95;
  --label:#e8e8e8;
  --portrait-a:#4a4a4a;
  --portrait-b:#d8d8d8;
}
*{box-sizing:border-box;margin:0;padding:0}
html,body{width:1200px;height:960px;overflow:hidden}
body{
  font-family:"Open Sans",Arial,sans-serif;
  background:repeating-linear-gradient(90deg,var(--board) 0 23px,var(--board-light) 23px 26px,var(--board) 26px 61px,#171717 61px 63px);
  position:relative;color:var(--ink);
}
.board-title{position:absolute;left:109px;top:62px;font-size:40px;font-weight:300;color:#fff}
.size-label{position:absolute;font-size:21px;font-weight:300;color:var(--label);white-space:nowrap}

.banner{position:absolute;overflow:hidden;background:var(--panel)}
.backdrop{position:absolute;background:linear-gradient(90deg,var(--sky) 0%,var(--sky-deep) 30%,var(--sky-deep) 70%,var(--sky) 100%)}
.backdrop::after{content:"";position:absolute;inset:0;background:linear-gradient(180deg,rgba(31,176,230,.25),rgba(31,176,230,0) 70%)}
.backdrop-faint{position:absolute;background:linear-gradient(90deg,#e6e9ec,#d6dade 50%,#e8eaec)}
.portrait{position:absolute;border-radius:50%;background:radial-gradient(circle at 50% 40%,var(--portrait-b),var(--portrait-a));box-shadow:0 0 0 6px rgba(255,255,255,.25)}
.portrait.recent{background:radial-gradient(circle at 50% 40%,#f4f4f4,#9a9a9a)}
.tagline{position:absolute;color:var(--ink);white-space:nowrap;
  text-shadow:-2px 0 #fff,2px 0 #fff,0 -2px #fff,0 2px #fff,-1px -1px #fff,1px 1px #fff,-1px 1px #fff,1px -1px #fff}
.tagline b{font-weight:700}
.contact{position:absolute;text-align:center;white-space:nowrap}
.contact .name{font-weight:700}
.contact .phone{color:var(--accent);font-weight:600}
.brokerage{position:absolute;display:flex;align-items:center;gap:6px;color:var(--brand);font-weight:700;white-space:nowrap}
.brokerage .mark{border-radius:50%;background:var(--brand);flex:none}

/* 1200 x 628 */
.banner-large{left:109px;top:188px;width:960px;height:502px}
.banner-large .backdrop{left:0;top:0;width:960px;height:326px}
.banner-large .backdrop-faint{left:0;top:326px;width:960px;height:176px;opacity:.8}
.banner-large .tagline{left:146px;top:284px;font-size:38px;font-weight:400;text-shadow:-3px 0 #fff,3px 0 #fff,0 -3px #fff,0 3px #fff,-2px -2px #fff,2px 2px #fff,-2px 2px #fff,2px -2px #fff}
.banner-large .contact{left:200px;width:600px;top:372px;font-size:26px}
.banner-large .url{display:block;margin-top:12px;font-size:22px;letter-spacing:12px;font-weight:400}
.banner-large .brokerage{left:22px;top:400px;font-size:20px}
.banner-large .brokerage .mark{width:30px;height:30px}

/* 320 x 250 */
.banner-box{left:109px;top:712px;width:240px;height:200px}
.banner-box .backdrop{left:0;top:0;width:240px;height:124px}
.banner-box .tagline{left:11px;top:109px;font-size:12px;text-shadow:-1px 0 #fff,1px 0 #fff,0 -1px #fff,0 1px #fff}
.banner-box .contact{left:92px;width:142px;top:138px;font-size:11.5px;line-height:18px}
.banner-box .brokerage{left:10px;top:158px;font-size:9px;line-height:11px;gap:4px}
.banner-box .brokerage .mark{width:14px;height:14px}

/* 728 x 90 */
.banner-leader{left:367px;top:712px;width:582px;height:72px}
.banner-leader .backdrop{left:0;top:0;width:338px;height:72px}
.banner-leader .tagline{left:181px;top:13px;font-size:15px;line-height:20px;text-shadow:-1px 0 #fff,1px 0 #fff,0 -1px #fff,0 1px #fff}
.banner-leader .contact{left:420px;width:156px;top:13px;font-size:12px;line-height:17px}
.banner-leader .brokerage{left:346px;top:29px;font-size:9px;gap:4px}
.banner-leader .brokerage .mark{width:12px;height:12px}

/* 320 x 50 */
.banner-mobile{left:367px;top:803px;width:256px;height:40px}
.banner-mobile .backdrop{left:0;top:0;width:158px;height:40px}
.banner-mobile .tagline{left:74px;top:12px;font-size:8px;line-height:11px;text-shadow:-1px 0 #fff,1px 0 #fff,0 -1px #fff,0 1px #fff}
.banner-mobile .contact{left:184px;width:70px;top:4px;font-size:5.5px;line-height:9px}
.banner-mobile .contact .name{font-size:6.5px}
.banner-mobile .brokerage{left:160px;top:11px;width:24px;flex-direction:column;font-size:3.5px;line-height:5px;gap:2px}
.banner-mobile .brokerage .mark{width:8px;height:8px}
</style>
</head>
<body>
  <h1 class="board-title">Banner Design Set</h1>
  <span class="size-label" style="left:963px;top:140px">1200 x 628</span>

  <section class="banner banner-large">
    <div class="backdrop" role="img" aria-label="Blue-tinted photo of a downtown Vancouver building facade"></div>
    <div class="backdrop-faint" role="img" aria-label="Faded photo of heritage building windows"></div>
    <div class="portrait" role="img" aria-label="Black and white portrait of the agent as a teenager in 1990" style="left:348px;top:148px;width:144px;height:144px"></div>
    <div class="portrait recent" role="img" aria-label="Recent portrait of the agent in suit and glasses" style="left:491px;top:140px;width:144px;height:144px"></div>
    <p class="tagline">Keeping it <b>"real"</b> estate since the <b>90's</b></p>
    <div class="brokerage"><span class="mark"></span>Harbourline Realty</div>
    <div class="contact">
      <span class="name">Morvyn Hale</span> | Call Me: <span class="phone">(604) 555-0142</span>
      <span class="url">www.agentmorvyn.net</span>
    </div>
  </section>

  <section class="banner banner-box">
    <div class="backdrop" role="img" aria-label="Blue-tinted photo of a downtown building"></div>
    <div class="portrait" role="img" aria-label="Black and white portrait of the agent in 1990" style="left:73px;top:64px;width:48px;height:48px;box-shadow:0 0 0 3px rgba(255,255,255,.25)"></div>
    <div class="portrait recent" role="img" aria-label="Recent portrait of the agent" style="left:125px;top:66px;width:48px;height:48px;box-shadow:0 0 0 3px rgba(255,255,255,.25)"></div>
    <p class="tagline">Keeping it <b>"real"</b> estate since the <b>90's</b></p>
    <div class="brokerage"><span class="mark"></span><span>Harbourline<br>Realty</span></div>
    <div class="contact">
      <div class="name">Morvyn Hale</div>
      <div>Call Me: <span class="phone">(604) 555-0142</span></div>
      <div>www.agentmorvyn.net</div>
    </div>
  </section>
  <span class="size-label" style="left:185px;top:916px">320 x250</span>

  <section class="banner banner-leader">
    <div class="backdrop" role="img" aria-label="Blue-tinted photo of a downtown building"></div>
    <div class="portrait" role="img" aria-label="Black and white portrait of the agent in 1990" style="left:38px;top:9px;width:64px;height:64px;box-shadow:0 0 0 4px rgba(255,255,255,.25)"></div>
    <div class="portrait recent" role="img" aria-label="Recent portrait of the agent" style="left:106px;top:10px;width:64px;height:64px;box-shadow:0 0 0 4px rgba(255,255,255,.25)"></div>
    <p class="tagline">Keeping it <b>"real"</b><br>estate since the <b>90's</b></p>
    <div class="brokerage"><span class="mark"></span><span>Harbourline<br>Realty</span></div>
    <div class="contact">
      <div class="name">Morvyn Hale</div>
      <div>Call Me: <span class="phone">(604) 555-0142</span></div>
      <div>www.agentmorvyn.net</div>
    </div>
  </section>
  <span class="size-label" style="left:966px;top:733px">728 x 90</span>

  <section class="banner banner-mobile">
    <div class="backdrop" role="img" aria-label="Blue-tinted photo of a downtown building"></div>
    <div class="portrait" role="img" aria-label="Black and white portrait of the agent in 1990" style="left:0;top:3px;width:34px;height:34px;box-shadow:0 0 0 2px rgba(255,255,255,.25)"></div>
    <div class="portrait recent" role="img" aria-label="Recent portrait of the agent" style="left:37px;top:3px;width:34px;height:34px;box-shadow:0 0 0 2px rgba(255,255,255,.25)"></div>
    <p class="tagline">Keeping it <b>"real"</b><br>estate since the <b>90's</b></p>
    <div class="brokerage"><span class="mark"></span><span>Harbourline</span></div>
    <div class="contact">
      <div class="name">Morvyn Hale</div>
      <div>Call Me: <span class="phone">(604) 555-0142</span></div>
      <div>www.agentmorvyn.net</div>
    </div>
  </section>
  <span class="size-label" style="left:636px;top:810px">320 x 50</span>
</body>
</html>
```